A property investment company, looking to provide lovely sustainable homes for familys and individua

For a small investment business i am starting which will buy and refurbish unloved houses and apartments to rent out or resell. the company name is my family surname (HARGREAVE). <br/>i would like the design to be simple with maybe some emphasis on an ethical and sustainable/environmentally friendly approach with a branding of maybe trees blended with some houses and or apartments.<br/>The colours i like for this design would be mainly green on either a white or black background.
Target Market(s)
This business card is to be used for professional people such as estate agents
mortgage brokers, solicitors and trades people.
Industry/Entity Type
Real Estate
Contact Information for Business Card
owner/director-Martin hargreave
e-mail-martin@hvholdings.co.uk
website-hargreavehomeholdings.co.uk
mobile-07700945318
landline-02079460581
Look and feel

```html
<!DOCTYPE html>
<html lang="en">
<head>
<meta charset="UTF-8">
<title>Hargreave Property Investments – Business Card</title>
<link href="https://fonts.googleapis.com/css2?family=Chakra+Petch:wght@400;500;600&display=swap" rel="stylesheet">
<style>
  :root {
    --backdrop: #2b2b2b;
    --paper: #eeeeee;
    --green-deep: #2f8f55;
    --green-brand: #2a8a4c;
    --green-mid: #6da673;
    --green-soft: #86b98a;
    --green-pale: #b3d6b1;
    --green-lime: #7cc46e;
    --green-edge: #4aa56d;
    --white: #ffffff;
  }
  * { margin: 0; padding: 0; box-sizing: border-box; }
  html, body {
    width: 1200px; height: 854px; overflow: hidden;
    background: var(--backdrop);
    font-family: "Chakra Petch", sans-serif;
  }
  .canvas {
    position: relative; width: 1200px; height: 854px;
    display: flex; align-items: center; justify-content: center; gap: 40px;
  }
  .card {
    position: relative; width: 550px; height: 355px; overflow: hidden;
    box-shadow: 0 18px 40px rgba(0,0,0,.55);
  }

  /* Front */
  .card-front { background: var(--paper); }
  .front-panel { position: absolute; right: 0; width: 178px; height: 50%; }
  .front-panel.top { top: 0; background: var(--green-soft); }
  .front-panel.bottom { bottom: 0; background: var(--green-mid); }
  .wordmark { position: absolute; text-align: center; white-space: nowrap; }
  .front-wordmark { left: 72px; top: 78px; width: 220px; }
  .wordmark-name { display: block; font-weight: 600; letter-spacing: 1px; line-height: 1; }
  .front-wordmark .wordmark-name { font-size: 34px; color: var(--green-brand); }
  .wordmark-tag { display: block; letter-spacing: 1.6px; margin-top: 3px; }
  .front-wordmark .wordmark-tag { font-size: 9px; color: var(--green-lime); }
  .contact { position: absolute; left: 39px; top: 200px; color: var(--green-brand); white-space: nowrap; }
  .contact-name { font-size: 24px; font-weight: 500; line-height: 1; }
  .contact-role { font-size: 9px; letter-spacing: 1.6px; color: var(--green-lime); margin: 3px 0 10px 22px; }
  .contact-line { font-size: 19px; line-height: 26px; letter-spacing: .3px; }

  /* Back */
  .card-back { background: var(--green-deep); }
  .back-block { position: absolute; }
  .back-block.top-left { left: 0; top: 0; width: 179px; height: 179px; background: var(--green-mid); }
  .back-block.top-mid { left: 179px; top: 0; width: 181px; height: 179px; background: var(--green-pale); }
  .back-block.bottom-left { left: 0; top: 179px; width: 179px; height: 176px; background: #65a36c; }
  .back-edge { position: absolute; right: 0; top: 0; width: 60px; height: 355px; }
  .back-wordmark { left: 240px; top: 245px; width: 240px; }
  .back-wordmark .wordmark-name { font-size: 36px; color: var(--white); }
  .back-wordmark .wordmark-tag { font-size: 11px; color: var(--white); margin-top: 2px; }
</style>
</head>
<body>
<main class="canvas">
  <section class="card card-front" aria-label="Business card front">
    <div class="front-panel top"></div>
    <div class="front-panel bottom"></div>
    <div class="wordmark front-wordmark">
      <span class="wordmark-name">HARGREAVE</span>
      <span class="wordmark-tag">PROPERTY INVESTMENTS</span>
    </div>
    <div class="contact">
      <p class="contact-name">Orlin Hargreave</p>
      <p class="contact-role">DIRECTOR</p>
      <p class="contact-line">07700 900318</p>
      <p class="contact-line">hargreavehomes.example</p>
      <p class="contact-line">orlin@hvholdings.example</p>
    </div>
  </section>

  <section class="card card-back" aria-label="Business card back">
    <div class="back-block top-left"></div>
    <div class="back-block top-mid"></div>
    <div class="back-block bottom-left"></div>
    <svg class="back-edge" viewBox="0 0 60 355" role="img" aria-label="Fine hatched arc along the right edge">
      <path d="M60 0 L44 0 Q 10 177 44 355 L60 355 Z" fill="var(--green-edge)"/>
    </svg>
    <div class="wordmark back-wordmark">
      <span class="wordmark-name">HARGREAVE</span>
      <span class="wordmark-tag">PROPERTY INVESTMENTS</span>
    </div>
  </section>
</main>
</body>
</html>
```